Website Refresh Needed - Large Couples Therapy Group

We are a large couples counselling group in Australia, and we have some key pages of our website that need refreshing, as it's a few years old now.
Similar colour palette as currently, and the same colours as the logo. No new logo required.
Total of 7 new (updated) page templates designs are needed:
1. HOME: https://www.thewillowlane.com.au/
2: CONTACT US: https://www.thewillowlane.com.au/contact/
3: RC CITY PAGE: https://www.thewillowlane.com.au/city/sydney/
4: ST CITY PAGE: https://www.thewillowlane.com.au/our-counselling/sex-therapy/sex-therapy-sydney/
5: ALL BLOGS: https://www.thewillowlane.com.au/blog/
6: BLOG: https://www.thewillowlane.com.au/sexual-desires-in-men-and-women-what-are-the-real-differences/
7: MAIN STANDARD PAGE: https://www.thewillowlane.com.au/our-counselling/couples-relationship-counselling/

Target Market(s)

couples who are going through a crisis in their relationship or marriage.

Number of Pages Required

5+ page

Colors
86cfc6
b8a6cd
cfdfed

Requirements
Must have
• Calm, reassuring colours. People are stressed and need to know we can help.
Should not have
• No bright oranges or yellows.

```html
<!DOCTYPE html>
<html lang="en">
<head>
<meta charset="utf-8">
<title>The Willow Lane – Blog</title>
<link href="https://fonts.googleapis.com/css2?family=Lato:wght@400;700;900&display=swap" rel="stylesheet">
<style>
:root{
  --teal:#86cfc6;
  --teal-text:#6cc2b6;
  --teal-deep:#1f6f7b;
  --lilac:#b8a6cd;
  --mist:#cfdfed;
  --ink:#2b2b2b;
  --ink-soft:#555;
  --rule:#e4e4e4;
  --footer-bg:#f4f4f4;
  --hero-bg:#f2f1ef;
}
*{box-sizing:border-box;margin:0;padding:0}
html,body{width:1200px;height:2887px;overflow:hidden}
body{position:relative;background:#fff;font-family:'Lato',sans-serif;color:var(--ink)}
.abs{position:absolute}

/* header */
.site-header{position:absolute;left:0;top:0;width:1200px;height:96px;border-bottom:1px solid var(--mist)}
.brand{position:absolute;left:73px;top:26px;display:flex;align-items:center;gap:12px}
.brand-dot{width:40px;height:40px;border-radius:50%;background:var(--teal-deep)}
.brand-name{font-size:32px;font-weight:400;color:var(--teal-deep);letter-spacing:.3px}
.top-nav a{position:absolute;top:37px;font-size:16px;color:#444;text-decoration:none}
.top-nav .active{font-weight:700;color:var(--ink)}
.vrule{position:absolute;top:32px;width:1px;height:32px;background:#ccc}
.search-icon{position:absolute;left:835px;top:36px}
.phone{position:absolute;left:914px;top:30px;display:flex;align-items:center;gap:6px;font-size:27px;font-weight:700;color:var(--ink)}

.sub-nav{position:absolute;left:0;top:97px;width:1200px;height:65px;border-bottom:2px solid var(--rule)}
.sub-nav a{position:absolute;top:23px;font-size:14px;color:var(--ink);text-decoration:none;white-space:nowrap}
.sub-nav .current{font-weight:700}
.sub-nav .underline{position:absolute;left:72px;top:60px;width:84px;height:4px;background:var(--teal)}

/* hero */
.hero{position:absolute;left:0;top:163px;width:1200px;height:405px;background:var(--hero-bg);border-bottom:2px solid var(--rule)}
.hero-photo{position:absolute;left:443px;top:0;width:757px;height:405px;background:linear-gradient(100deg,#efe9e0 0%,#e4b9a0 35%,#b8565a 60%,#d9c6b2 100%)}
.hero-title{position:absolute;left:147px;top:168px;width:280px;text-align:center;font-size:40px;font-weight:900;color:var(--ink)}

/* latest */
.section-title{position:absolute;left:0;top:640px;width:1200px;text-align:center;font-size:35px;font-weight:400;color:var(--ink)}
.section-title strong{font-weight:900}

.feature{position:absolute;width:453px}
.feature .photo{width:453px;height:256px}
.feature .meta{margin:30px 0 0 11px;font-size:14px;color:#444}
.feature .title{margin:10px 0 0 11px;font-size:19.5px;font-weight:700;line-height:27px;color:#333;text-transform:uppercase}
.feature .excerpt{margin:14px 0 0 11px;font-size:13.5px;line-height:22px;color:var(--ink-soft)}
.learn{display:inline-block;color:var(--teal-text);font-weight:700;text-decoration:none;text-transform:uppercase}
.feature .learn{margin:14px 0 0 13px;font-size:16.5px}

.tile{position:absolute;width:217px}
.tile .photo{width:217px;height:164px}
.tile .title{margin:23px 0 0 6px;font-size:17px;font-weight:700;line-height:22px;color:#333;text-transform:uppercase}
.tile .learn{margin:16px 0 0 6px;font-size:13px}

.view-more{position:absolute;left:505px;top:2390px;width:185px;height:51px;border-radius:26px;background:var(--teal);color:#fff;font-size:16px;font-weight:700;display:flex;align-items:center;justify-content:center;text-decoration:none}

/* footer */
.site-footer{position:absolute;left:0;top:2454px;width:1200px;height:433px;background:var(--footer-bg)}
.footer-arc{position:absolute;left:0;top:0}
.footer-brand{position:absolute;left:0;top:112px;width:1200px;display:flex;justify-content:center;align-items:center;gap:12px}
.footer-links{position:absolute;left:0;top:200px;width:1200px;text-align:center;font-size:17px;color:#333}
.footer-links .sep{margin:0 12px}
.footer-links b{font-weight:700}
.footer-nav{position:absolute;left:0;top:255px;width:1200px;display:flex;justify-content:center;gap:22px;font-size:12px;color:#333}
.copyright{position:absolute;left:0;top:291px;width:1200px;text-align:center;font-size:13px;color:#777}
.social{position:absolute;left:539px;top:333px;display:flex;gap:4px}
.social span{width:38px;height:38px;border:2px solid #333;border-radius:50%;display:block}
</style>
</head>
<body>

<header class="site-header">
  <div class="brand"><span class="brand-dot"></span><span class="brand-name">The Willow Lane</span></div>
  <nav class="top-nav">
    <a class="active" style="left:519px">HOME</a>
    <a style="left:629px">FAQS</a>
    <a style="left:731px">BLOG</a>
  </nav>
  <span class="vrule" style="left:812px"></span>
  <svg class="search-icon" width="24" height="24" viewBox="0 0 24 24" fill="none" stroke="#b8a6cd" stroke-width="3"><circle cx="10" cy="10" r="7"/><line x1="15" y1="15" x2="21" y2="21"/></svg>
  <span class="vrule" style="left:885px"></span>
  <div class="phone">
    <svg width="26" height="26" viewBox="0 0 24 24" fill="none" stroke="#b8a6cd" stroke-width="2"><path d="M5 3h4l2 5-3 2a12 12 0 0 0 6 6l2-3 5 2v4a2 2 0 0 1-2 2A18 18 0 0 1 3 5a2 2 0 0 1 2-2z"/></svg>
    1300 555 019
  </div>
</header>

<nav class="sub-nav">
  <a class="current" style="left:76px">ABOUT US</a>
  <a style="left:170px">COUNSELLING TYPES</a>
  <a style="left:335px">RELATIONSHIP COUNSELLING LOCATIONS</a>
  <a style="left:637px">SEX THERAPY LOCATIONS</a>
  <a style="left:832px">QUIZZES</a>
  <a style="left:914px">FEES &amp; REBATE</a>
  <a style="left:1039px">CONTACT US</a>
  <span class="underline"></span>
</nav>

<section class="hero">
  <div class="hero-photo" role="img" aria-label="Happy couple playing piggyback outdoors in a sunny street"></div>
  <h1 class="hero-title">OUR BLOGS</h1>
</section>

<h2 class="section-title">LATEST <strong>BLOGS</strong></h2>

<article class="feature" style="left:123px;top:724px">
  <div class="photo" role="img" aria-label="Couple kissing on a bicycle under a cloudy sky" style="background:linear-gradient(180deg,#9cc3e6 0%,#d8e6f0 55%,#7c9a4c 100%)"></div>
  <p class="meta">April 12, 2019 &nbsp;|&nbsp; No Comments</p>
  <h3 class="title">Mauris vel lacus vitae felis vestibulum volutpat etiam est nunc</h3>
  <p class="excerpt">Nunc tempus felis vitae urna Vivamus porttitor neque at volutpat rutrum purus nisi eleifend libero a tempus libero lectus</p>
  <a class="learn">Learn More</a>
</article>
<article class="feature" style="left:612px;top:724px">
  <div class="photo" role="img" aria-label="Couple holding hands looking at the sea" style="background:linear-gradient(180deg,#5d9fd6 0%,#7db6e0 40%,#1f4f7a 60%,#6a6a66 100%)"></div>
  <p class="meta">April 12, 2019 &nbsp;|&nbsp; No Comments</p>
  <h3 class="title">Mauris vel lacus vitae felis vestibulum volutpat etiam est nunc</h3>
  <p class="excerpt">Nunc tempus felis vitae urna Vivamus porttitor neque at volutpat rutrum purus nisi eleifend libero a tempus libero lectus</p>
  <a class="learn">Learn More</a>
</article>
<article class="feature" style="left:131px;top:1242px">
  <div class="photo" role="img" aria-label="Stressed woman on a phone call" style="background:linear-gradient(135deg,#eeeeee 0%,#c9c9c9 50%,#e8e8e8 100%)"></div>
  <p class="meta">April 12, 2019 &nbsp;|&nbsp; No Comments</p>
  <h3 class="title">Mauris vel lacus vitae felis vestibulum volutpat etiam est nunc</h3>
  <p class="excerpt">Nunc tempus felis vitae urna Vivamus porttitor neque at volutpat rutrum purus nisi eleifend libero a tempus libero lectus</p>
  <a class="learn">Learn More</a>
</article>
<article class="feature" style="left:621px;top:1242px">
  <div class="photo" role="img" aria-label="Groom kissing bride with a flower crown on the forehead" style="background:linear-gradient(90deg,#dfe1df 0%,#c7b39e 50%,#4a3a32 100%)"></div>
  <p class="meta">April 12, 2019 &nbsp;|&nbsp; No Comments</p>
  <h3 class="title">Mauris vel lacus vitae felis vestibulum volutpat etiam est nunc</h3>
  <p class="excerpt">Nunc tempus felis vitae urna Vivamus porttitor neque at volutpat rutrum purus nisi eleifend libero a tempus libero lectus</p>
  <a class="learn">Learn More</a>
</article>

<article class="tile" style="left:143px;top:1763px">
  <div class="photo" role="img" aria-label="Laughing couple embracing" style="background:linear-gradient(135deg,#6f86a0,#b99883)"></div>
  <h3 class="title">How normal is it to watch porn?</h3>
  <a class="learn">Learn More</a>
</article>
<article class="tile" style="left:383px;top:1763px">
  <div class="photo" role="img" aria-label="Upset couple sitting apart on a sofa" style="background:linear-gradient(135deg,#d9d6d2,#8b7f78)"></div>
  <h3 class="title">Letter for a partner doubtful about relationship</h3>
  <a class="learn">Learn More</a>
</article>
<article class="tile" style="left:623px;top:1763px">
  <div class="photo" role="img" aria-label="Smiling couple hugging" style="background:linear-gradient(135deg,#c9d3da,#3b5a80)"></div>
  <h3 class="title">Is your pursuit of success sabotaging your relationships</h3>
  <a class="learn">Learn More</a>
</article>
<article class="tile" style="left:863px;top:1763px">
  <div class="photo" role="img" aria-label="Couple on a swing at sunset by the sea" style="background:linear-gradient(180deg,#d7c3b0,#e9a25e 55%,#5a4336)"></div>
  <h3 class="title">Have you lost yourself in your relationship?</h3>
  <a class="learn">Learn More</a>
</article>

<article class="tile" style="left:147px;top:2065px">
  <div class="photo" role="img" aria-label="Couple smiling under a white sheet" style="background:linear-gradient(135deg,#c9793f,#e9d8c6)"></div>
  <h3 class="title">What is narcissism and what is narcissistic</h3>
  <a class="learn">Learn More</a>
</article>
<article class="tile" style="left:386px;top:2065px">
  <div class="photo" role="img" aria-label="Worried woman with a man in the background" style="background:linear-gradient(90deg,#e2dccf,#c3ccd2)"></div>
  <h3 class="title">Recovering from an affair</h3>
  <a class="learn">Learn More</a>
</article>
<article class="tile" style="left:626px;top:2065px">
  <div class="photo" role="img" aria-label="Couple lying together on a bed" style="background:linear-gradient(135deg,#8a6d63,#d8c2d0)"></div>
  <h3 class="title">6 step to becoming an emotionally available lover</h3>
  <a class="learn">Learn More</a>
</article>
<article class="tile" style="left:866px;top:2065px">
  <div class="photo" role="img" aria-label="Woman shouting through a traffic cone at a man" style="background:linear-gradient(90deg,#f1ede6,#d94a3a 50%,#4c4f4a)"></div>
  <h3 class="title">Coupling throught coronavirus</h3>
  <a class="learn">Learn More</a>
</article>

<a class="view-more">VIEW MORE</a>

<footer class="site-footer">
  <svg class="footer-arc" width="1200" height="90" viewBox="0 0 1200 90">
    <path d="M0 0 Q600 130 1200 0 L1200 -1 L0 -1 Z" fill="#fff"/>
    <path d="M180 34 Q600 118 1040 30" fill="none" stroke="#b8a6cd" stroke-width="4" opacity=".8"/>
  </svg>
  <div class="footer-brand"><span class="brand-dot"></span><span class="brand-name">The Willow Lane</span></div>
  <p class="footer-links">Associate Enquiry<span class="sep">|</span>Member Login<span class="sep">|</span><b>1300 555 019</b></p>
  <nav class="footer-nav">
    <span>ABOUT US</span><span>COUNSELLING TYPES</span><span>RELATIONSHIP COUNSELLING LOCATIONS</span><span>SEX THERAPY LOCATIONS</span><span>QUIZZES</span><span>FEES &amp; REBATE</span><span>CONTACT US</span>
  </nav>
  <p class="copyright">© 2020 Company Name | All Rights Reserved</p>
  <div class="social">
    <span aria-label="Social link"></span><span aria-label="Social link"></span><span aria-label="Social link"></span><span aria-label="Social link"></span>
  </div>
</footer>

</body>
</html>
```